Professional finish needed to powerpoint slides

I am pitching my business for investment and have two pages as part of the business plan called the 'Quillmarsh Orbit' and the 'Built by the Tollbrook Orbit'.
They are basically visual one page plans to help investors see if the business is worth investing in or not. You only need to take the pages with the diagram in, so 2 pages in total.
The Orbit can be given an edge to make it look info graphic style.
Good luck

```html
<!DOCTYPE html>
<html lang="en">
<head>
<meta charset="utf-8">
<title>Quillmarsh Orbit</title>
<link rel="stylesheet" href="https://fonts.googleapis.com/css2?family=Arimo:wght@400;700&family=Libre+Baskerville:wght@700&display=swap">
<style>
  :root {
    --bg: #ffffff;
    --heading: #3a3a3a;
    --brand: #1f6e2c;
    --hub: #3a3a3a;
    --badge: #3d3d3d;
    --ink-light: #ffffff;
    --ink-dark: #3b3b3b;
    --profit: #d8262f;
    --revenue: #e2622a;
    --subscribers: #f6a51e;
    --segments: #f7d21a;
    --product: #8cc440;
    --marketing: #17a68a;
    --sales: #1d9bd8;
    --operations: #2c3290;
    --skills: #6a50a2;
    --people: #d8255b;
  }
  html, body { margin: 0; padding: 0; overflow: hidden; background: var(--bg); }
  .canvas { width: 1200px; height: 1020px; overflow: hidden; position: relative; }
  .orbit { display: block; width: 1200px; height: 1020px; }
  .sector-profit { fill: var(--profit); }
  .sector-revenue { fill: var(--revenue); }
  .sector-subscribers { fill: var(--subscribers); }
  .sector-segments { fill: var(--segments); }
  .sector-product { fill: var(--product); }
  .sector-marketing { fill: var(--marketing); }
  .sector-sales { fill: var(--sales); }
  .sector-operations { fill: var(--operations); }
  .sector-skills { fill: var(--skills); }
  .sector-people { fill: var(--people); }
  .ring-tint { fill: #ffffff; fill-opacity: 0.13; }
  .hub { fill: var(--hub); }
  .year-badge { fill: var(--badge); }
  .year-label { font-family: "Arimo", sans-serif; font-weight: 700; font-size: 11px; fill: var(--ink-light); text-anchor: middle; }
  .heading { font-family: "Libre Baskerville", serif; font-weight: 700; font-size: 16px; fill: var(--heading); text-anchor: middle; }
  .note { font-family: "Arimo", sans-serif; font-size: 10px; fill: var(--ink-light); }
  .note-dark { font-family: "Arimo", sans-serif; font-size: 10px; fill: var(--ink-dark); }
  .note-large { font-size: 10.5px; }
  .figure { font-family: "Arimo", sans-serif; font-weight: 700; font-size: 11px; fill: var(--ink-light); text-anchor: middle; }
  .mid { text-anchor: middle; }
  .bold { font-weight: 700; }
  .brand-mark { fill: var(--brand); }
  .brand-name { font-family: "Arimo", sans-serif; font-weight: 700; font-size: 26px; fill: var(--brand); }
</style>
</head>
<body>
<div class="canvas">
<svg class="orbit" viewBox="0 0 960 816" xmlns="http://www.w3.org/2000/svg" role="img" aria-label="Quillmarsh Orbit business plan diagram, 2013 to 2016">

  <g class="brand">
    <rect class="brand-mark" x="20" y="42" width="18" height="18"/>
    <text class="brand-name" x="46" y="60">Quillmarsh</text>
  </g>

  <g class="sectors">
    <path class="sector-profit" d="M490 402 L428.4 52.4 A355 355 0 0 1 667.5 94.6 Z"/>
    <path class="sector-revenue" d="M490 402 L667.5 94.6 A355 355 0 0 1 797.4 224.5 Z"/>
    <path class="sector-subscribers" d="M490 402 L797.4 224.5 A355 355 0 0 1 845 402 Z"/>
    <path class="sector-segments" d="M490 402 L845 402 A355 355 0 0 1 780.8 605.6 Z"/>
    <path class="sector-product" d="M490 402 L780.8 605.6 A355 355 0 0 1 640 723.7 Z"/>
    <path class="sector-marketing" d="M490 402 L640 723.7 A355 355 0 0 1 218.1 630.2 Z"/>
    <path class="sector-sales" d="M490 402 L218.1 630.2 A355 355 0 0 1 140.4 463.6 Z"/>
    <path class="sector-operations" d="M490 402 L140.4 463.6 A355 355 0 0 1 156.4 280.6 Z"/>
    <path class="sector-skills" d="M490 402 L156.4 280.6 A355 355 0 0 1 239 151 Z"/>
    <path class="sector-people" d="M490 402 L239 151 A355 355 0 0 1 428.4 52.4 Z"/>
  </g>

  <g class="year-rings">
    <circle class="ring-tint" cx="490" cy="402" r="275"/>
    <circle class="ring-tint" cx="490" cy="402" r="200"/>
    <circle class="ring-tint" cx="490" cy="402" r="125"/>
  </g>

  <circle class="hub" cx="490" cy="402" r="50"/>

  <g class="years">
    <rect class="year-badge" x="545" y="396" width="56" height="23" rx="3"/>
    <text class="year-label" x="573" y="411">2013</text>
    <rect class="year-badge" x="628" y="396" width="53" height="23" rx="3"/>
    <text class="year-label" x="654" y="411">2014</text>
    <rect class="year-badge" x="703" y="396" width="53" height="23" rx="3"/>
    <text class="year-label" x="729" y="411">2015</text>
    <rect class="year-badge" x="771" y="396" width="56" height="23" rx="3"/>
    <text class="year-label" x="799" y="411">2016</text>
  </g>

  <g class="headings">
    <text class="heading" x="470" y="35">NET PROFIT</text>
    <text class="heading" x="724" y="92">REVENUE</text>
    <text class="heading" x="870" y="227">SUBSCRIBERS</text>
    <text class="heading" x="852" y="598">MARKET</text>
    <text class="heading" x="858" y="620">SEGMENTS</text>
    <text class="heading" x="722" y="725">PRODUCT</text>
    <text class="heading" x="722" y="748">MIX</text>
    <text class="heading" x="477" y="785">MARKETING</text>
    <text class="heading" x="127" y="583">DIRECT</text>
    <text class="heading" x="127" y="605">SALES</text>
    <text class="heading" x="73" y="410">OPERATIONS</text>
    <text class="heading" x="146" y="193">SKILLS/</text>
    <text class="heading" x="146" y="215">TRAINING</text>
    <text class="heading" x="307" y="80">PEOPLE</text>
  </g>

  <g class="net-profit">
    <text class="figure" x="487" y="104">£300k</text>
    <text class="figure" x="487" y="187">£150k</text>
    <text class="figure" x="484" y="259">£91k</text>
    <text class="figure" x="487" y="317">£3,179</text>
  </g>

  <g class="revenue">
    <text class="figure" x="643" y="156">£1m</text>
    <text class="figure" x="608" y="220">£500k</text>
    <text class="figure" x="575" y="275">£300k</text>
    <text class="note mid" x="549" y="326">£179,175</text>
    <text class="note mid" x="549" y="339">(100kSwr)</text>
  </g>

  <g class="subscribers">
    <text class="note-dark mid" x="757" y="264">418 @</text>
    <text class="note-dark mid" x="757" y="279">£299</text>
    <text class="note-dark mid" x="684" y="299">209 @</text>
    <text class="note-dark mid" x="684" y="314">£299</text>
    <text class="note-dark mid" x="633" y="332">104 @</text>
    <text class="note-dark mid" x="633" y="347">£299</text>
    <text class="note-dark mid" x="573" y="366">35</text>
  </g>

  <g class="market-segments">
    <text class="note-dark" x="602" y="455">(Avoid PR Market)</text>
    <text class="note-dark" x="602" y="469">London/B'ham Tech</text>
    <text class="note-dark" x="602" y="483">Govt Corp Suppliers</text>
    <text class="note-dark" x="602" y="497">Mkt Global Private Biz</text>
    <text class="note-dark" x="638" y="517">Diversification, Agency Market</text>
    <text class="note-dark" x="638" y="531">(criteria robust product)Top</text>
    <text class="note-dark" x="638" y="545">100 Companies To Work For</text>
    <text class="note-dark" x="704" y="570">Planned Evolution</text>
    <text class="note-dark" x="704" y="584">with Markets</text>
  </g>

  <g class="product-mix">
    <text class="note-dark note-large" x="491" y="477">Software 56%,</text>
    <text class="note-dark note-large" x="491" y="493">(Mng PR, P Blast, 3</text>
    <text class="note-dark note-large" x="491" y="509">Rport Ad – 44%)</text>
    <text class="note-dark mid" x="573" y="526">Software</text>
    <text class="note-dark mid" x="573" y="540">90%, Press</text>
    <text class="note-dark mid" x="573" y="554">Blast 10%</text>
    <text class="note-dark mid" x="598" y="609">100%</text>
    <text class="note-dark mid" x="634" y="675">100%</text>
  </g>

  <g class="marketing">
    <text class="note mid" x="441" y="550">Webinars, Kestrel, Awareness London</text>
    <text class="note mid" x="441" y="564">M'chster, Develop Brand /Val. Prop., Lead</text>
    <text class="note mid" x="441" y="578">Gen. Campaigns, Searchly Ad, e-shots,</text>
    <text class="note mid" x="441" y="592">Target Regions, Mystery Shopping, Online</text>
    <text class="note mid" x="441" y="606">Demos, Introduce A Pro-active Sales Process</text>
    <text class="note mid" x="441" y="620">&amp; Monitoring, Company Product * “In</text>
    <text class="note mid" x="441" y="634">House” Capabilities – Identify Through</text>
    <text class="note mid" x="441" y="648">Media (Research) Database AIM Listed plc's</text>
    <text class="note mid" x="452" y="672">App.,In House Developers, In House Media, Data</text>
    <text class="note mid" x="452" y="686">Control, Social Network, Journalist Bloggers</text>
    <text class="note mid" x="452" y="720">Review &amp; Continual  Adaption Related to</text>
    <text class="note mid" x="452" y="734">Market &amp; New Technologies</text>
  </g>

  <g class="direct-sales">
    <text class="note" x="347" y="446">10-20 plc's, Visit</text>
    <text class="note" x="347" y="460">Website &amp; get 3</text>
    <text class="note" x="347" y="474">contacts on each ,</text>
    <text class="note" x="347" y="488">run pilot – Mkting,</text>
    <text class="note" x="347" y="502">Comms, HR, Fin.,</text>
    <text class="note" x="347" y="516">MD, Chair</text>
    <text class="note" x="251" y="490">Establish</text>
    <text class="note" x="251" y="503">“Quillmarsh” Way</text>
    <text class="note" x="251" y="516">– Implement,</text>
    <text class="note" x="251" y="529">Continually</text>
    <text class="note" x="251" y="542">Monitor &amp;</text>
    <text class="note" x="251" y="555">Review</text>
    <text class="note-dark mid" x="210" y="552">As</text>
    <text class="note-dark mid" x="210" y="565">Year 2</text>
  </g>

  <g class="operations">
    <text class="note" x="237" y="359">Consolidate</text>
    <text class="note" x="237" y="372">UK, More</text>
    <text class="note" x="237" y="385">Global</text>
    <text class="note" x="237" y="398">Markets</text>
    <text class="note" x="237" y="411">(planned)</text>
    <text class="note" x="307" y="374">Resellers, Franchise,</text>
    <text class="note" x="307" y="387">Partners Europe,</text>
    <text class="note" x="307" y="400">Manchester, London,</text>
    <text class="note" x="307" y="413">Global Markets Pull</text>
  </g>

  <g class="skills-training">
    <text class="note mid bold" x="357" y="329">Bring in skills</text>
    <text class="note mid bold" x="357" y="343">(buy in)</text>
  </g>

  <g class="people">
    <text class="note" x="305" y="123">Chief Technical Officer,</text>
    <text class="note" x="305" y="137">4 Sales People</text>
    <text class="note" x="305" y="151">London/Manchester</text>
    <text class="note" x="327" y="188">In house Media x 2,</text>
    <text class="note" x="327" y="202">Team – Chirper – 2</text>
    <text class="note" x="327" y="216">Sales People</text>
    <text class="note" x="327" y="230">London/Manchester</text>
    <text class="note" x="376" y="271">2 Sales Person</text>
    <text class="note mid" x="440" y="330">1 Sales</text>
    <text class="note mid" x="440" y="344">Person</text>
  </g>

</svg>
</div>
</body>
</html>
```